Brochure Cover Design Project

I am a real estate agent in West Vancouver British Columbia Canada.
I have some branding I like as can be seen on my web site, but would like a cover page I can use for the presentations I bind.
I would like to use my current banner and then perhaps have some random photos of places I've sold with a SOLD banner over the corner of each photo. I'm open to ideas. Perhaps I can use the
Gus-tatory paragraph that is on the front page of my web site as well.

Target Market(s)

My audience is older than younger and upper class, so nothing targeting a very young audience.

Industry/Entity Type

Real Estate

Requirements
Nice to have
• I can supply an number of high res photos that can be used as part of the cover page.
I would like the cover page to be in a format where I could change the feature home photos as needed.

```html
<!DOCTYPE html>
<html lang="en">
<head>
<meta charset="utf-8">
<title>Reid Calloway – Presentation Cover</title>
<link rel="stylesheet" href="https://fonts.googleapis.com/css2?family=Open+Sans:ital,wght@0,400;0,700;1,400&family=Tinos:wght@700&family=Arimo:ital,wght@0,400;0,700;1,700&display=swap">
<style>
  :root {
    --backdrop: #e9e6e1;
    --page-top: #a4c8de;
    --page-bottom: #cde5f2;
    --ink: #1c1c1c;
    --gold: #e8b418;
    --gold-edge: #5a4300;
    --rule: #7a8d99;
    --frame: #ffffff;
    --ribbon: #c3121a;
    --sky-deep: #3f78bf;
    --sky-light: #a9cdea;
    --house-light: #cdb898;
    --house-dark: #8a6f55;
    --lawn: #5f8f3c;
    --lawn-dark: #35582a;
    --strip: #3b3578;
    --strip-text: #f4d35e;
    --strip-light: #e6e9f5;
  }
  * { box-sizing: border-box; margin: 0; padding: 0; }
  html, body { width: 1200px; height: 900px; overflow: hidden; }
  body { background: var(--backdrop); position: relative; font-family: "Open Sans", sans-serif; color: var(--ink); }

  .cover {
    position: absolute; left: 270px; top: 22px; width: 660px; height: 856px;
    background: linear-gradient(180deg, var(--page-top) 0%, var(--page-bottom) 100%);
    overflow: hidden; box-shadow: 0 6px 18px rgba(0,0,0,.25);
  }

  .listing {
    position: absolute; width: 138px; height: 90px;
    border: 4px solid var(--frame);
    box-shadow: 0 2px 5px rgba(0,0,0,.3);
    overflow: hidden;
  }
  .listing-photo {
    position: absolute; inset: 0;
    background:
      linear-gradient(90deg, rgba(40,70,30,.55) 0%, rgba(40,70,30,0) 22%, rgba(40,70,30,0) 72%, rgba(40,70,30,.6) 100%),
      linear-gradient(180deg, var(--sky-deep) 0%, var(--sky-light) 22%, var(--house-light) 34%, var(--house-dark) 58%, var(--house-light) 68%, var(--lawn) 80%, var(--lawn-dark) 100%);
  }
  .sold-ribbon { position: absolute; left: 0; top: 0; width: 60px; height: 60px; }

  .agent-title {
    position: absolute; left: 180px; right: 20px; top: 36px; text-align: center;
    font-family: "Tinos", serif; font-weight: 700; font-size: 46px; color: var(--gold);
    -webkit-text-stroke: 1px var(--gold-edge);
  }

  .philosophy { position: absolute; left: 200px; width: 420px; top: 290px; }
  .philosophy h2 { text-align: center; font-size: 16px; font-weight: 700; margin-bottom: 26px; }
  .philosophy hr { border: 0; border-top: 1px solid var(--rule); }
  .philosophy p { font-size: 10.5px; font-style: italic; line-height: 1.42; text-align: justify; margin-top: 10px; }
  .philosophy p + p { margin-top: 14px; }
  .philosophy .rule-end { margin-top: 6px; }
  .signature { font-size: 15px; margin-top: 8px; margin-left: -4px; }

  .banner { position: absolute; left: 0; right: 0; bottom: 0; height: 160px; }
  .banner-scene {
    position: absolute; inset: 0 0 38px 0;
    background:
      linear-gradient(90deg, rgba(30,35,80,.35) 0%, rgba(30,35,80,0) 35%, rgba(30,35,80,0) 70%, rgba(30,35,80,.3) 100%),
      linear-gradient(180deg, #cfdcef 0%, #aebfe0 10%, #e8eef7 18%, #5c6aa3 30%, #3b4a86 48%, #8e9cc4 60%, #c2c9dc 68%, #6a86bd 80%, #4a6aa8 100%);
  }
  .banner-name {
    position: absolute; left: 24px; top: 26px;
    font-family: "Tinos", serif; font-weight: 700; font-size: 38px; color: var(--gold);
  }
  .agent-portrait {
    position: absolute; left: 340px; top: 14px; width: 110px; height: 146px;
    background: linear-gradient(180deg, #a98a76 0%, #7a5d4e 30%, #26262c 52%, #15151a 100%);
    border-radius: 50px 50px 0 0;
  }
  .brokerage {
    position: absolute; left: 466px; top: 28px; display: flex; align-items: center; gap: 6px;
    font-family: "Open Sans", sans-serif; font-weight: 700; font-size: 12px; color: #ffffff;
  }
  .brokerage .dot { width: 18px; height: 18px; border-radius: 50%; background: #ffffff; }
  .award-badge {
    position: absolute; right: 26px; top: 22px; width: 40px; height: 40px; border-radius: 50%;
    background: #b79a3e;
  }
  .contact-strip {
    position: absolute; left: 0; right: 0; bottom: 0; height: 38px; background: var(--strip);
    font-family: "Arimo", sans-serif;
  }
  .contact-strip .phone { position: absolute; left: 22px; top: 8px; font-size: 18px; font-weight: 700; color: var(--strip-text); }
  .contact-strip .web { position: absolute; left: 160px; top: 13px; font-size: 11px; font-style: italic; font-weight: 700; color: var(--strip-light); }
  .contact-strip .email { position: absolute; right: 22px; top: 13px; font-size: 11px; color: var(--strip-light); }
</style>
</head>
<body>
<main class="cover">

  <div class="listing" style="left:20px; top:24px"><div class="listing-photo" role="img" aria-label="Photo of a sold home"></div><svg class="sold-ribbon" viewBox="0 0 60 60"><polygon points="0,26 26,0 44,0 0,44" fill="var(--ribbon)"/><text x="14" y="26" transform="rotate(-45 14 26)" font-family="Arimo, sans-serif" font-weight="700" font-size="9" fill="#fff" text-anchor="middle">SOLD</text></svg></div>
  <div class="listing" style="left:20px; top:127px"><div class="listing-photo" role="img" aria-label="Photo of a sold home"></div><svg class="sold-ribbon" viewBox="0 0 60 60"><polygon points="0,26 26,0 44,0 0,44" fill="var(--ribbon)"/><text x="14" y="26" transform="rotate(-45 14 26)" font-family="Arimo, sans-serif" font-weight="700" font-size="9" fill="#fff" text-anchor="middle">SOLD</text></svg></div>
  <div class="listing" style="left:20px; top:230px"><div class="listing-photo" role="img" aria-label="Photo of a sold home"></div><svg class="sold-ribbon" viewBox="0 0 60 60"><polygon points="0,26 26,0 44,0 0,44" fill="var(--ribbon)"/><text x="14" y="26" transform="rotate(-45 14 26)" font-family="Arimo, sans-serif" font-weight="700" font-size="9" fill="#fff" text-anchor="middle">SOLD</text></svg></div>
  <div class="listing" style="left:20px; top:333px"><div class="listing-photo" role="img" aria-label="Photo of a sold home"></div><svg class="sold-ribbon" viewBox="0 0 60 60"><polygon points="0,26 26,0 44,0 0,44" fill="var(--ribbon)"/><text x="14" y="26" transform="rotate(-45 14 26)" font-family="Arimo, sans-serif" font-weight="700" font-size="9" fill="#fff" text-anchor="middle">SOLD</text></svg></div>
  <div class="listing" style="left:20px; top:436px"><div class="listing-photo" role="img" aria-label="Photo of a sold home"></div><svg class="sold-ribbon" viewBox="0 0 60 60"><polygon points="0,26 26,0 44,0 0,44" fill="var(--ribbon)"/><text x="14" y="26" transform="rotate(-45 14 26)" font-family="Arimo, sans-serif" font-weight="700" font-size="9" fill="#fff" text-anchor="middle">SOLD</text></svg></div>
  <div class="listing" style="left:20px; top:539px"><div class="listing-photo" role="img" aria-label="Photo of a sold home"></div><svg class="sold-ribbon" viewBox="0 0 60 60"><polygon points="0,26 26,0 44,0 0,44" fill="var(--ribbon)"/><text x="14" y="26" transform="rotate(-45 14 26)" font-family="Arimo, sans-serif" font-weight="700" font-size="9" fill="#fff" text-anchor="middle">SOLD</text></svg></div>

  <div class="listing" style="left:178px; top:160px"><div class="listing-photo" role="img" aria-label="Photo of a sold home"></div><svg class="sold-ribbon" viewBox="0 0 60 60"><polygon points="0,26 26,0 44,0 0,44" fill="var(--ribbon)"/><text x="14" y="26" transform="rotate(-45 14 26)" font-family="Arimo, sans-serif" font-weight="700" font-size="9" fill="#fff" text-anchor="middle">SOLD</text></svg></div>
  <div class="listing" style="left:330px; top:160px"><div class="listing-photo" role="img" aria-label="Photo of a sold home"></div><svg class="sold-ribbon" viewBox="0 0 60 60"><polygon points="0,26 26,0 44,0 0,44" fill="var(--ribbon)"/><text x="14" y="26" transform="rotate(-45 14 26)" font-family="Arimo, sans-serif" font-weight="700" font-size="9" fill="#fff" text-anchor="middle">SOLD</text></svg></div>
  <div class="listing" style="left:482px; top:160px"><div class="listing-photo" role="img" aria-label="Photo of a sold home"></div><svg class="sold-ribbon" viewBox="0 0 60 60"><polygon points="0,26 26,0 44,0 0,44" fill="var(--ribbon)"/><text x="14" y="26" transform="rotate(-45 14 26)" font-family="Arimo, sans-serif" font-weight="700" font-size="9" fill="#fff" text-anchor="middle">SOLD</text></svg></div>

  <h1 class="agent-title">Reid Calloway</h1>

  <section class="philosophy">
    <h2>GUS-TATORY</h2>
    <hr>
    <p>I believe the key to a good Realtor is KNOWLEDGE! I was born and raised on the North Shore of Vancouver B.C. and know the Lower Mainland well. With twenty seven years of sales &amp; management experience, I understand the business and I know how to negotiate the best possible outcome for my clients. I keep on top of ever-changing markets, trends, technologies and am advanced at social media use, to enhance and expand the reach of my listings and in turn, get the job done for you! I make it a point to get to know and understand the expressed needs and wants of my clients, whether buying or selling.</p>
    <p>I want to be your Realtor, even if it will be a while before you need one. When you are ready, with my experience and knowledge, I will ease you through the process.</p>
    <p>And... they say I'm a pretty nice guy!</p>
    <p>I am at your service!</p>
    <hr class="rule-end">
    <div class="signature">Reid Calloway</div>
  </section>

  <footer class="banner">
    <div class="banner-scene" role="img" aria-label="Panorama of snow-capped North Shore mountains over the city and harbour"></div>
    <div class="banner-name">Reid Calloway</div>
    <div class="agent-portrait" role="img" aria-label="Portrait of the agent"></div>
    <div class="brokerage"><span class="dot"></span>Summit Realty</div>
    <div class="award-badge" role="img" aria-label="Award badge"></div>
    <div class="contact-strip">
      <span class="phone">604 555 0182</span>
      <span class="web">www.ReidCalloway.com</span>
      <span class="email">rcalloway@mailbox.com</span>
    </div>
  </footer>
</main>
</body>
</html>
```